Landing page for buying gold and stamps

Create a landing page for our purchase. We buy postage stamps, franked goods, gold coins, scrap gold, silver money, etc. We don't want to sell anything to people, we just shop. So the visitors should send their old gold, their stamps, etc. by post. We then estimate the value and transfer the money by bank or you can collect it in cash.

The visitor should see what he can sell. If he fills in his contact details, he will receive our purchase form and the mailing label by post so that he can send in his sales goods free of charge. Or he can call us or write an e-mail and come to us directly.

We buy:
When the form is filled out, an email will be sent to our address with the following data:
Surname
First name
Street, Nr.
Post loan number
place
What do you want to sell

In the appendix I have added designs of flyers. You can see what we buy on it. What is missing on the flyer, however, are stamps, franking goods and rarities. In addition, the design should be similar. The logo can also be used.

In addition, the following text should be on the page:
Do you need help selling an inherited collection? Feel free to contact us. We are happy to help. We have been in the stamp and coin trade for nearly 100 years.

I have also attached a picture of the stamp as an attachment. This should also be put on the side with old gold and gold coins.

And here you will find our current purchase pages:
https://www.briefhaus-tanner.ch/ankauf-gold-und-silber
https://www.briefhaus-tanner.ch/ankauf-frankatur

Competitors' pages:
https://www.wertsachenpost.ch/goldankauf/
https://www.praegehof-lindt.ch/ankauf-1/altgold-ankauf1.html

Target Market(s)

Private persons

Font styles to use
Serif
Sans Serif

Requirements
Must have
• It must be clear that anyone who wants to sell their gold, stamps or coins can do so easily from home by post. You no longer have to go to a store.
Steps to Sell:
1. You fill out your contact details
2. We will send you a form and a label for shipping (no postage for you!)
3. You will receive a non-binding purchase offer
4. You will receive the money transferred or you can collect it in cash (or we will send you the valuables you have sent back)

You have no costs! Simply sell your gold or stamps from home.

```html
<!DOCTYPE html>
<html lang="de">
<head>
<meta charset="utf-8">
<title>Briefhaus Tanner – Ankauf Gold und Silber</title>
<link href="https://fonts.googleapis.com/css2?family=Poppins:ital,wght@0,400;0,500;0,600;1,500&family=Libre+Baskerville:wght@400;700&family=Oswald:wght@600&display=swap" rel="stylesheet">
<style>
:root{
  --navy:#0b0b4e;
  --red:#ee1c25;
  --indigo:#2e2e8f;
  --yellow:#fbcd56;
  --grey-bg:#f4f4f4;
  --text:#222;
  --muted:#444;
  --step1:#f0b52d;
  --step2:#9a63cf;
  --step3:#4433f2;
  --step4:#ee1c25;
  --violet-note:#7b6cf0;
}
*{margin:0;padding:0;box-sizing:border-box}
html,body{width:830px;height:1200px;overflow:hidden}
body{position:relative;background:#fff;font-family:'Poppins',sans-serif;color:var(--text)}
.abs{position:absolute}
.serif{font-family:'Libre Baskerville',serif}

.top-bar{left:0;top:0;width:830px;height:26px;background:var(--navy)}
.top-links{right:142px;top:8px;display:flex;gap:7px;font-size:6.5px;color:#fff}
.top-links span{display:flex;align-items:center;gap:3px}
.top-links i{display:inline-block;width:6px;height:6px;background:#fff;border-radius:50%}

.brand{font-weight:600;color:var(--red);font-size:17px;display:flex;align-items:center;gap:6px;white-space:nowrap}
.brand::before{content:"";width:12px;height:12px;background:var(--indigo);flex:none}
.site-brand{left:150px;top:47px}
.search{left:466px;top:48px;width:218px;height:17px;border-bottom:1px solid #888;font-size:6.5px;color:#666;padding-top:2px}
.search svg{position:absolute;right:2px;top:0}

.main-nav{left:0;top:92px;width:830px;height:26px;background:var(--red);display:flex;gap:15px;padding-left:148px;align-items:center;font-size:7.5px;color:#fff;white-space:nowrap}
.main-nav span::after{content:" ▾";font-size:6px}
.main-nav span.plain::after{content:""}

.crumbs{left:144px;top:126px;font-size:6.5px;color:#333}
.crumbs b{font-weight:400;color:var(--red)}

.slider{left:138px;top:143px;width:555px;height:183px;background:#fff;box-shadow:0 0 4px rgba(0,0,0,.18)}
.slide-arrow{top:221px;width:27px;height:27px;border:1.5px solid var(--indigo);border-radius:50%;display:flex;align-items:center;justify-content:center}
.dots{top:336px;left:405px;display:flex;gap:6px}
.dots i{width:8px;height:8px;border-radius:50%;border:1px solid var(--red)}
.dots i:first-child{background:var(--red)}
.offer-kicker{left:160px;top:170px;font-size:11px;font-weight:500}
.offer-title{left:156px;top:183px;font-size:31px;font-weight:700;color:var(--red)}
.offer-ticks{left:159px;top:224px;font-size:11px;font-weight:500;display:flex;gap:6px;align-items:center}
.offer-items{left:160px;top:254px;font-size:9px;font-weight:600;line-height:10.5px}
.offer-note{left:164px;top:296px;font-size:8.5px;font-style:italic;font-weight:500;color:#fff}

.help{left:0;top:361px;width:830px;height:245px;background:var(--grey-bg);text-align:center}
.eyebrow{font-size:14.5px;color:#222}
.headline{font-size:23px;font-weight:700;color:var(--indigo);letter-spacing:-.3px}
.lead{font-size:11px;color:#333;line-height:13px}
.call-btn{left:228px;top:504px;width:374px;height:47px;border:2px solid var(--red);border-radius:24px;padding:3px}
.call-btn div{width:100%;height:100%;background:var(--red);border-radius:20px;color:#fff;font-weight:600;font-size:21px;letter-spacing:2.6px;display:flex;align-items:center;justify-content:center}
.bank-note{left:0;width:830px;top:569px;text-align:center;font-size:11px;font-weight:600;color:var(--violet-note)}

.step{width:120px;text-align:center}
.step h3{font-size:10.5px;font-weight:600;margin-top:0;white-space:nowrap}
.step p{font-size:7.3px;line-height:10.4px;color:#444;text-align:left;margin-top:8px}
.step-num{font-family:'Oswald',sans-serif;font-size:21px;font-weight:600;color:#111}
.divider{width:1px;height:175px;background:#999;top:813px}
.divider::after{content:"";position:absolute;left:-2px;bottom:-3px;width:5px;height:5px;border-radius:50%;background:#999}

.footer{left:0;top:1060px;width:830px;height:121px;background:var(--navy);color:#fff}
.footer-logo{left:144px;top:30px;width:130px;height:64px;background:#fff;border-radius:5px;display:flex;align-items:center;justify-content:center}
.footer-logo .brand{font-size:12px;gap:5px}
.footer-logo .brand::before{width:9px;height:9px}
.footer-col{top:41px;font-size:6.5px;line-height:13px;white-space:nowrap}
.footer-col h4{font-size:8px;font-weight:500;margin-bottom:9px}
.bottom-bar{left:0;top:1181px;width:830px;height:19px;background:var(--red);color:#fff;font-size:6.5px;white-space:nowrap}
</style>
</head>
<body>

<div class="abs top-bar"></div>
<div class="abs top-links">
  <span><i></i>My Account</span>|<span><i></i>Wish List</span>|<span><i></i>Shoping Cart</span>|<span><i></i>Checkout</span>|<span><i></i>Register</span>
</div>

<div class="abs brand site-brand">Briefhaus Tanner</div>
<div class="abs search">Gesamten Shop dur
  <svg width="9" height="9" viewBox="0 0 10 10"><circle cx="4" cy="4" r="3" fill="none" stroke="#444" stroke-width="1.4"/><line x1="6.2" y1="6.2" x2="9" y2="9" stroke="#444" stroke-width="1.5"/></svg>
</div>

<nav class="abs main-nav">
  <span>Postage Stamps</span><span>Tanner - albums &amp; accessories</span><span>Coins &amp; Banknotes</span><span>Missing List Service</span><span class="plain">Franking Service</span><span>Purchases</span>
</nav>

<div class="abs crumbs">Home &nbsp;/ <b>Purchase of Gold and Silver</b></div>

<div class="abs slide-arrow" style="left:90px"><svg width="10" height="10" viewBox="0 0 10 10"><path d="M9 5H1M4.5 1.5L1 5l3.5 3.5" fill="none" stroke="var(--indigo)" stroke-width="1.6"/></svg></div>
<div class="abs slide-arrow" style="left:713px"><svg width="10" height="10" viewBox="0 0 10 10"><path d="M1 5h8M5.5 1.5L9 5 5.5 8.5" fill="none" stroke="var(--indigo)" stroke-width="1.6"/></svg></div>

<div class="abs slider">
  <svg class="abs" style="left:7px;top:8px" width="540" height="168" viewBox="0 0 540 168">
    <path d="M0 0H334C300 30 285 80 300 125L317 168H0Z" fill="var(--yellow)"/>
    <path d="M0 139H296L317 168H0Z" fill="var(--red)"/>
  </svg>
  <div role="img" aria-label="Goldmünzen und Silbermünzen" class="abs" style="left:332px;top:12px;width:218px;height:107px;background:radial-gradient(circle at 70% 50%,#c9c9c9,#8a8a8a 35%,transparent 36%),radial-gradient(circle at 30% 50%,#e8b54a,#b98320 60%,#fff 61%)"></div>
  <div class="abs" style="left:336px;top:120px;width:214px;height:41px;border:2px solid #9a6a2c;display:flex">
    <div role="img" aria-label="Goldschmuck, Ringe und Ketten" style="flex:1;background:linear-gradient(135deg,#f3e2b3,#c8952e);border-right:2px solid #9a6a2c"></div>
    <div role="img" aria-label="Goldbarren" style="flex:1;background:linear-gradient(135deg,#f7eed2,#d79c25);border-right:2px solid #9a6a2c"></div>
    <div role="img" aria-label="Goldmünzen gestapelt" style="flex:1.2;background:linear-gradient(135deg,#f7ecd0,#dfa530)"></div>
  </div>
</div>
<div class="abs offer-kicker">wir suchen und kaufen</div>
<div class="abs serif offer-title">GOLD &amp; SILBER</div>
<div class="abs offer-ticks">
  <svg width="14" height="14" viewBox="0 0 14 14"><circle cx="7" cy="7" r="5.5" fill="none" stroke="var(--red)" stroke-width="1.4"/><path d="M4 7l2.2 2.2L12 3" fill="none" stroke="var(--red)" stroke-width="1.5"/></svg>
  <span>&nbsp;sicher</span>
  <svg width="14" height="14" viewBox="0 0 14 14"><circle cx="7" cy="7" r="5.5" fill="none" stroke="var(--red)" stroke-width="1.4"/><path d="M4 7l2.2 2.2L12 3" fill="none" stroke="var(--red)" stroke-width="1.5"/></svg>
  <span>Transparenz</span>
  <svg width="14" height="14" viewBox="0 0 14 14"><circle cx="7" cy="7" r="5.5" fill="none" stroke="var(--red)" stroke-width="1.4"/><path d="M4 7l2.2 2.2L12 3" fill="none" stroke="var(--red)" stroke-width="1.5"/></svg>
  <span>fair</span>
</div>
<div class="abs offer-items">Goldvreneli &nbsp;| &nbsp;altgold und silber &nbsp;| &nbsp;Münzen &nbsp;| &nbsp;Barren &nbsp;|<br>Medaillen &nbsp;| &nbsp;Uhren &nbsp;| &nbsp;Ringe &nbsp;| &nbsp;Ketten</div>
<div class="abs offer-note">***Durchsuchen Sie ihren Haushaltes könnte sicj lohnen!</div>
<div class="abs dots"><i></i><i></i></div>

<section class="abs help">
  <div class="serif eyebrow" style="margin-top:31px">Do you need help selling an</div>
  <div class="serif headline" style="margin-top:3px">INHERITED COLLECTION?</div>
  <p class="lead" style="margin-top:12px">Feel free to contact us. We are happy to help. We have been in<br>the stamp and coin trade for nearly 100 years.</p>
</section>
<div class="abs call-btn"><div>CALL 0041 61 555 20 40</div></div>
<div class="abs bank-note">*** wir bezahlen mehr für Goldvreneli als ihre Bank ***</div>

<section class="abs" style="left:0;top:632px;width:830px;text-align:center">
  <div class="serif eyebrow">Steps to Sell</div>
  <div class="serif headline" style="margin-top:2px">HOW IT WORKS?</div>
  <p class="lead" style="margin-top:12px;color:#555">Gold und Silber konnen Sie ins auch per Einschreiben zustellen.<br>Die Auszahlung efrfolgt innerhalb 48 Stunden.</p>
</section>

<svg class="abs" style="left:160px;top:750px" width="520" height="46" viewBox="0 0 520 46">
  <g font-family="Poppins,sans-serif" font-weight="600" font-size="11" fill="#fff">
    <g transform="translate(10,0)"><path d="M4 10H56L66 1 76 22 56 43 58 34H4L8 22Z" fill="var(--step1)"/><path d="M4 34L0 42 10 34Z" fill="var(--step1)" opacity=".7"/><text x="14" y="27">Step 1</text></g>
    <g transform="translate(144,0)"><path d="M4 10H56L66 1 76 22 56 43 58 34H4L8 22Z" fill="var(--step2)"/><path d="M4 34L0 42 10 34Z" fill="var(--step2)" opacity=".7"/><text x="14" y="27">Step 2</text></g>
    <g transform="translate(300,0)"><path d="M4 10H56L66 1 76 22 56 43 58 34H4L8 22Z" fill="var(--step3)"/><path d="M4 34L0 42 10 34Z" fill="var(--step3)" opacity=".7"/><text x="14" y="27">Step 3</text></g>
    <g transform="translate(434,0)"><path d="M4 10H56L66 1 76 22 56 43 58 34H4L8 22Z" fill="var(--step4)"/><path d="M4 34L0 42 10 34Z" fill="var(--step4)" opacity=".7"/><text x="14" y="27">Step 4</text></g>
  </g>
</svg>

<svg class="abs" style="left:170px;top:803px" width="490" height="40" viewBox="0 0 490 40" fill="none" stroke-width="1.2">
  <g stroke="var(--step1)"><rect x="2" y="3" width="22" height="30"/><path d="M6 10h14M6 15h14M6 20h10M6 25h8M30 6L20 30 18 34 22 31 32 8Z"/></g>
  <g stroke="var(--step2)" transform="translate(150,0)"><path d="M2 8L11 1 20 8V35H2Z"/><circle cx="11" cy="8" r="2"/><rect x="6" y="15" width="10" height="14"/><path d="M8 19h6M8 22h6M8 25h6"/></g>
  <g stroke="var(--step3)" transform="translate(294,0)"><path d="M18 1l4 5 6-2 1 6 6 2-2 6 4 4-4 4 2 6-6 2-1 6-6-2-4 5-4-5-6 2-1-6-6-2 2-6-4-4 4-4-2-6 6-2 1-6 6 2Z" stroke-width="1.4"/><rect x="2" y="15" width="32" height="10" rx="3"/><text x="18" y="24" text-anchor="middle" font-family="Poppins,sans-serif" font-size="9" font-weight="600" fill="var(--step3)" stroke="none">BUY</text></g>
  <g stroke="var(--step4)" transform="translate(442,0)"><rect x="1" y="20" width="6" height="13"/><path d="M7 23c6-3 10-3 14 0h7c3 0 3 3 0 3h-9M7 31c6 2 12 2 18-1l9-6c2-2 0-4-2-3l-7 4"/><text x="18" y="14" text-anchor="middle" font-family="Poppins,sans-serif" font-size="13" fill="var(--step4)" stroke="none">€</text></g>
</svg>

<div class="abs divider" style="left:261px"></div>
<div class="abs divider" style="left:409px"></div>
<div class="abs divider" style="left:557px"></div>

<div class="abs step" style="left:126px;top:855px"><h3>Fill Contact Form</h3><p style="padding-left:15px">Fill Your Contact details and send it to us. You cna find the contact form in the conatct page.</p></div>
<div class="abs step" style="left:274px;top:855px;width:124px"><h3>Form &amp; Label Send</h3><p style="padding-left:10px">We will send you a form and a label for shipping (no posage for you!). This label will be used to send your item to us.</p></div>
<div class="abs step" style="left:421px;top:855px;width:128px"><h3>Purchase Offer</h3><p style="padding-left:21px">You will receive a non -bind-ing purchase offer where you can see the price we offer or any other conditions.</p></div>
<div class="abs step" style="left:566px;top:855px;width:128px"><h3>Receive Money</h3><p style="padding-left:14px">You will received the money transferrred or you can collect it in cash( or we wil send you the valuables you have sent back).</p></div>

<div class="abs step-num" style="left:177px;top:956px">01</div>
<div class="abs step-num" style="left:323px;top:956px">02</div>
<div class="abs step-num" style="left:470px;top:956px">03</div>
<div class="abs step-num" style="left:614px;top:956px">04</div>

<svg class="abs" style="left:140px;top:996px" width="540" height="8" viewBox="0 0 540 8">
  <g stroke-width="1.3">
    <line x1="5" y1="4" x2="88" y2="4" stroke="var(--step1)"/><circle cx="5" cy="4" r="2.5" fill="var(--step1)"/><circle cx="88" cy="4" r="2.5" fill="var(--step1)"/>
    <line x1="153" y1="4" x2="236" y2="4" stroke="var(--step2)"/><circle cx="153" cy="4" r="2.5" fill="var(--step2)"/><circle cx="236" cy="4" r="2.5" fill="var(--step2)"/>
    <line x1="300" y1="4" x2="383" y2="4" stroke="var(--step3)"/><circle cx="300" cy="4" r="2.5" fill="var(--step3)"/><circle cx="383" cy="4" r="2.5" fill="var(--step3)"/>
    <line x1="444" y1="4" x2="527" y2="4" stroke="var(--step4)"/><circle cx="444" cy="4" r="2.5" fill="var(--step4)"/><circle cx="527" cy="4" r="2.5" fill="var(--step4)"/>
  </g>
</svg>

<footer class="abs footer">
  <div class="abs footer-logo"><div class="brand">Briefhaus Tanner</div></div>
  <div class="abs footer-col" style="left:318px"><h4>Customer Service</h4>Guarantee of Trust<br>Shipping</div>
  <div class="abs footer-col" style="left:426px"><h4>Contact</h4>Contact<br>Imprint</div>
  <div class="abs footer-col" style="left:500px"><h4>Information</h4>Conditions<br>Revocation<br>Data Protection</div>
  <div class="abs footer-col" style="left:592px;top:40px"><h4>Unser Direktkontakt</h4>
    <div style="display:flex;gap:10px"><svg width="7" height="7" viewBox="0 0 8 8" style="margin-top:3px"><path d="M1 1l2-.5 1 2-1 1c.5 1 1.3 1.8 2.3 2.3l1-1 2 1L7 8C3.5 7.5.5 4.5 1 1Z" fill="var(--red)"/></svg><span>+41 (0) 61 555 20 40</span></div>
    <div style="display:flex;gap:10px"><svg width="7" height="6" viewBox="0 0 8 6" style="margin-top:7px;flex:none"><rect width="8" height="6" fill="var(--red)"/><path d="M0 0l4 3 4-3" fill="none" stroke="var(--navy)" stroke-width=".8"/></svg><span>oder senden Sie uns eine<br>Email</span></div>
  </div>
</footer>
<div class="abs bottom-bar">
  <span class="abs" style="left:146px;top:5px">© 2020, All Rights Reserved, Briefhaus Tanner</span>
  <span class="abs" style="left:565px;top:5px;display:flex;gap:8px;align-items:center"><i style="width:5px;height:5px;background:#fff;border-radius:50%;display:inline-block"></i>www.sozialseite.ch/briefhaustanner</span>
</div>

</body>
</html>
```